Business Card Design for Portrait photography professional

We are a small company specializing in portrait photography (weddings, family, couples, children, newborn, pregnant, etc.) Occasionally we do business portraits too and do some other type of photography. We need a business card which would fit into the same look and feel as our website theme (lumvira.com - under construction currently).
Our target customer base lies within mid- to upmarket. We want our business cards to convey a feeling of quality, solidness and a bit luxury.
Design should be universal and usable on 85mmx55mm, 90mmx50mm and 90mmx55mm
one extra file (PSD of a website didn't fit into the allowed updoad, therefore has put it into my dropbox: https://www.filqueso.com/s/qt8wr3kadhy5lbv/website%20theme%20PSD.psd)

Target Market(s)

mostly private people, 25-60 years old, mostly well established.

Industry/Entity Type

Portrait Photography

Requirements
Must have
• 2 sided design (print on both sides of the business card).
Must include:
business name, logo, URL (lumvira.no) , employee name, email address, and phone number.
Colorscheme of the website lumvira.no / lumvira.com

```html
<!DOCTYPE html>
<html lang="en">
<head>
<meta charset="utf-8">
<title>Lumvira – Business Card</title>
<link rel="stylesheet" href="https://fonts.googleapis.com/css2?family=Open+Sans:wght@400;600;700&display=swap">
<style>
  :root {
    --backdrop: #e9e5df;
    --card: #2b2927;
    --ink: #f3f1ec;
    --ink-soft: #c9c6c0;
    --rule: #8a8783;
    --shadow: rgba(0, 0, 0, 0.28);
  }
  * { box-sizing: border-box; margin: 0; padding: 0; }
  html, body {
    width: 1200px;
    height: 720px;
    overflow: hidden;
    background: var(--backdrop);
    font-family: "Open Sans", Arial, sans-serif;
    color: var(--ink);
  }
  .sheet {
    width: 1200px;
    height: 720px;
    display: flex;
    align-items: center;
    justify-content: center;
    gap: 40px;
  }
  .card {
    position: relative;
    width: 540px;
    height: 300px;
    background: var(--card);
    border-radius: 4px;
    box-shadow: 0 10px 26px var(--shadow);
    overflow: hidden;
  }

  /* Front side */
  .brand-mark {
    position: absolute;
    left: 30px;
    top: 26px;
    display: flex;
    align-items: center;
    gap: 14px;
  }
  .brand-mark__circle {
    width: 96px;
    height: 96px;
    border: 3px solid var(--ink);
    border-radius: 50%;
  }
  .brand-mark__name {
    font-size: 22px;
    font-weight: 600;
    letter-spacing: 0.06em;
    color: var(--ink);
  }
  .employee {
    position: absolute;
    left: 34px;
    bottom: 40px;
  }
  .employee__name {
    font-size: 19px;
    font-weight: 700;
    color: var(--ink);
  }
  .employee__title {
    font-size: 13px;
    color: var(--ink-soft);
    margin-top: 2px;
  }
  .divider {
    position: absolute;
    left: 336px;
    top: 150px;
    width: 1px;
    height: 112px;
    background: var(--rule);
  }
  .contact {
    position: absolute;
    left: 354px;
    top: 160px;
    list-style: none;
  }
  .contact__item {
    display: flex;
    align-items: center;
    gap: 8px;
    font-size: 13.5px;
    color: var(--ink);
    line-height: 1;
    margin-bottom: 14px;
  }
  .contact__icon {
    width: 12px;
    height: 12px;
    flex: none;
  }

  /* Back side */
  .emblem {
    position: absolute;
    left: 50%;
    top: 36px;
    transform: translateX(-50%);
    width: 180px;
    height: 180px;
    border: 3px solid var(--ink);
    border-radius: 50%;
    display: flex;
    align-items: center;
    justify-content: center;
  }
  .emblem__name {
    font-size: 26px;
    font-weight: 600;
    letter-spacing: 0.08em;
    color: var(--ink);
  }
  .web-address {
    position: absolute;
    left: 0;
    right: 0;
    bottom: 36px;
    text-align: center;
    font-size: 15px;
    letter-spacing: 0.22em;
    color: var(--ink-soft);
  }
</style>
</head>
<body>
<main class="sheet">
  <section class="card card--front" aria-label="Business card, contact side">
    <div class="brand-mark">
      <span class="brand-mark__circle" aria-hidden="true"></span>
      <span class="brand-mark__name">Lumvira</span>
    </div>

    <div class="employee">
      <p class="employee__name">Employee name</p>
      <p class="employee__title">Title</p>
    </div>

    <span class="divider" aria-hidden="true"></span>

    <ul class="contact">
      <li class="contact__item">
        <svg class="contact__icon" viewBox="0 0 12 12" aria-hidden="true">
          <circle cx="6" cy="6" r="6" fill="var(--ink)"/>
          <path d="M4 3.2 L5 4.8 L4.5 5.4 Q5.3 6.9 6.6 7.5 L7.2 7 L8.8 8 L8.2 9 Q5 8.8 3.2 4 Z" fill="var(--card)"/>
        </svg>
        123-456-0198
      </li>
      <li class="contact__item">
        <svg class="contact__icon" viewBox="0 0 12 12" aria-hidden="true">
          <circle cx="6" cy="6" r="6" fill="var(--ink)"/>
          <rect x="3" y="4" width="6" height="4.2" fill="var(--card)"/>
          <path d="M3 4 L6 6.4 L9 4" stroke="var(--ink)" stroke-width="0.8" fill="none"/>
        </svg>
        info@lumvira.com
      </li>
      <li class="contact__item">
        <svg class="contact__icon" viewBox="0 0 12 12" aria-hidden="true">
          <circle cx="6" cy="6" r="6" fill="var(--ink)"/>
          <circle cx="6" cy="6" r="3.4" fill="none" stroke="var(--card)" stroke-width="0.9"/>
          <ellipse cx="6" cy="6" rx="1.4" ry="3.4" fill="none" stroke="var(--card)" stroke-width="0.8"/>
          <line x1="2.6" y1="6" x2="9.4" y2="6" stroke="var(--card)" stroke-width="0.8"/>
        </svg>
        www.lumvira.com
      </li>
    </ul>
  </section>

  <section class="card card--back" aria-label="Business card, brand side">
    <div class="emblem">
      <span class="emblem__name">Lumvira</span>
    </div>
    <p class="web-address">www.lumvira.com</p>
  </section>
</main>
</body>
</html>
```